Simple elegant business card

General card for a fin and television director.
Just want name, email, phone and address.

Target Market(s)

Prospective employers

Industry/Entity Type

Business

Requirements
Must have
• As above
Nice to have
• Logo but not necessary.
Should not have
• Not too colourful or funky.
• Simplicity and elegance the way to go.

```html
<!DOCTYPE html>
<html lang="en">
<head>
<meta charset="utf-8">
<title>Nora Hale — Business Card</title>
<link rel="stylesheet" href="https://fonts.googleapis.com/css2?family=Barlow:wght@400;500&family=Quicksand:wght@300&display=swap">
<style>
  :root {
    --backdrop: #1d1d1d;
    --card-front: #f1f1f1;
    --card-back: #2b2b2b;
    --ink-dark: #333333;
    --ink-soft: #4a4a4a;
    --ink-light: #e8e8e8;
    --accent-red: #d8322c;
  }
  html, body {
    margin: 0;
    padding: 0;
    width: 1200px;
    height: 900px;
    overflow: hidden;
    background: var(--backdrop);
  }
  .canvas {
    position: relative;
    width: 1200px;
    height: 900px;
  }
  .card {
    position: absolute;
    left: 360px;
    width: 477px;
    height: 268px;
    box-sizing: border-box;
  }
  .card-front {
    top: 166px;
    background: var(--card-front);
    font-family: "Barlow", sans-serif;
    color: var(--ink-dark);
  }
  .card-back {
    top: 476px;
    background: var(--card-back);
    display: flex;
    align-items: center;
    justify-content: center;
  }
  .name-mark {
    position: absolute;
    left: 29px;
    top: 49px;
    display: flex;
    align-items: center;
  }
  .name-dot {
    width: 8px;
    height: 8px;
    border-radius: 50%;
    background: var(--accent-red);
    margin-right: 26px;
  }
  .name-front {
    font-size: 16px;
    font-weight: 500;
    letter-spacing: 0.2px;
  }
  .contact-list {
    position: absolute;
    left: 63px;
    top: 109px;
    margin: 0;
  }
  .contact-item {
    margin: 0 0 11px 0;
  }
  .contact-label {
    display: block;
    font-size: 11px;
    font-weight: 500;
    line-height: 13px;
    color: var(--ink-dark);
  }
  .contact-value {
    display: block;
    font-size: 13px;
    font-weight: 400;
    line-height: 16px;
    color: var(--ink-soft);
  }
  .name-back {
    font-family: "Quicksand", sans-serif;
    font-weight: 300;
    font-size: 46px;
    letter-spacing: 1px;
    color: var(--ink-light);
    margin-top: 4px;
  }
</style>
</head>
<body>
<main class="canvas">
  <section class="card card-front">
    <div class="name-mark">
      <span class="name-dot"></span>
      <span class="name-front">Nora Hale</span>
    </div>
    <dl class="contact-list">
      <div class="contact-item">
        <dt class="contact-label">telephone</dt>
        <dd class="contact-value" style="margin:0">+1 310 555 0142</dd>
      </div>
      <div class="contact-item">
        <dt class="contact-label">e-mail</dt>
        <dd class="contact-value" style="margin:0">norahale@example.com</dd>
      </div>
      <div class="contact-item">
        <dt class="contact-label">address</dt>
        <dd class="contact-value" style="margin:0">14 Harbor Lane, Sausalito, CA 94965</dd>
      </div>
    </dl>
  </section>
  <section class="card card-back">
    <div class="name-back">Nora Hale</div>
  </section>
</main>
</body>
</html>
```